Business Card - Apex Wellness

Please use the logo / design elements and font to design a business card that is eye catching and informative. If using "Direct Primary Care" logo element, you don't have to spell it out in the text.

Dr. Brendan Halvik
Apex Wellness - Direct Primary Care
4817 Tillbrook Rd. Suite 305
Millbrook Falls, AR 72099
Phone: 479-555-0137
ApexWellnessAR.example

```html
<!DOCTYPE html>
<html lang="en">
<head>
<meta charset="utf-8">
<title>Apex Wellness – Business Card</title>
<link href="https://fonts.googleapis.com/css2?family=Montserrat:wght@400;500;700;800&display=swap" rel="stylesheet">
<style>
  :root {
    --navy: #0b1537;
    --navy-soft: #1d2f6b;
    --royal: #3a5fb0;
    --sky: #3fb6e6;
    --white: #ffffff;
    --ink: #1a2140;
    --stage: #2e2e30;
  }
  * { box-sizing: border-box; margin: 0; padding: 0; }
  html, body {
    width: 1200px; height: 875px; overflow: hidden;
    background: var(--stage);
    font-family: "Montserrat", sans-serif;
  }
  .sheet {
    width: 1200px; height: 875px;
    display: flex; align-items: center; justify-content: center; gap: 40px;
  }
  .card {
    position: relative;
    width: 540px; height: 309px;
    border-radius: 22px;
    overflow: hidden;
  }

  /* Back */
  .card-back { background: var(--navy); }
  .back-lockup {
    position: absolute; left: 50%; top: 50%;
    transform: translate(-50%, -50%);
    text-align: center;
  }
  .back-name {
    font-size: 52px; font-weight: 500; letter-spacing: -0.5px;
    color: var(--navy-soft); white-space: nowrap;
  }
  .back-rule {
    margin: 10px auto 0; width: 360px; height: 1px;
    background: var(--navy-soft);
  }

  /* Front */
  .card-front { background: var(--white); }
  .front-panel { position: absolute; inset: 0; }
  .front-content {
    position: absolute; left: 34px; top: 34px; width: 300px;
    color: var(--ink);
  }
  .brand-name {
    font-size: 30px; font-weight: 500; letter-spacing: -0.4px;
    color: var(--navy); white-space: nowrap;
  }
  .brand-rule { margin-top: 8px; width: 250px; height: 1px; background: var(--navy); }
  .person { margin-top: 30px; position: relative; }
  .person-marker {
    position: absolute; left: -34px; top: 6px;
    width: 16px; height: 26px; background: var(--royal);
  }
  .person-name {
    font-size: 17px; font-weight: 800; text-transform: uppercase;
    color: var(--navy); letter-spacing: 0.2px; white-space: nowrap;
  }
  .person-title { font-size: 12px; font-weight: 400; margin-top: 2px; }
  .address { margin-top: 14px; font-size: 11.5px; line-height: 1.45; }
  .contacts { margin-top: 14px; list-style: none; font-size: 11.5px; line-height: 1.7; }
  .contacts li { display: flex; align-items: center; gap: 7px; white-space: nowrap; }
  .contacts svg { width: 11px; height: 11px; flex: none; }
  .web-accent { color: var(--royal); }
</style>
</head>
<body>
<main class="sheet">

  <section class="card card-back" aria-label="Card back">
    <div class="back-lockup">
      <div class="back-name">Apex Wellness</div>
      <div class="back-rule"></div>
    </div>
  </section>

  <section class="card card-front" aria-label="Card front">
    <svg class="front-panel" viewBox="0 0 540 309" preserveAspectRatio="none" aria-hidden="true">
      <path d="M330 0 H540 V309 H390 C360 240 345 180 352 110 C356 60 345 25 330 0 Z" fill="var(--navy)"/>
    </svg>

    <div class="front-content">
      <div class="brand-name">Apex Wellness</div>
      <div class="brand-rule"></div>

      <div class="person">
        <span class="person-marker"></span>
        <div class="person-name">Dr. Brendan Halvik</div>
        <div class="person-title">CEO/Founder</div>
      </div>

      <div class="address">
        4817 Tillbrook Rd. Suite 305<br>
        Millbrook Falls, AR 72099
      </div>

      <ul class="contacts">
        <li>
          <svg viewBox="0 0 24 24"><path fill="var(--sky)" d="M6.6 10.8a15.1 15.1 0 0 0 6.6 6.6l2.2-2.2c.3-.3.7-.4 1-.2 1.1.4 2.3.6 3.6.6.6 0 1 .4 1 1V20c0 .6-.4 1-1 1A17 17 0 0 1 3 4c0-.6.4-1 1-1h3.5c.6 0 1 .4 1 1 0 1.3.2 2.5.6 3.6.1.3 0 .7-.2 1z"/></svg>
          479-555-0137
        </li>
        <li>
          <svg viewBox="0 0 24 24"><rect x="2" y="5" width="20" height="14" rx="2" fill="var(--sky)"/><path d="M3 6l9 7 9-7" stroke="#fff" stroke-width="1.8" fill="none"/></svg>
          info@ApexWellnessAR.example
        </li>
        <li>
          <svg viewBox="0 0 24 24"><circle cx="12" cy="12" r="10" fill="var(--sky)"/><path d="M2 12h20M12 2c3 3 3 17 0 20M12 2c-3 3-3 17 0 20" stroke="#fff" stroke-width="1.4" fill="none"/></svg>
          <span>www.<span class="web-accent">ApexWellnessAR</span>.example</span>
        </li>
      </ul>
    </div>
  </section>

</main>
</body>
</html>
```